Tovik Lumen - Magazine

Our client would like a magazine designed for a conceptual novelty based on unconventional views on contemporary issues, including; finance, religion, politics etc.!

The novelty includes 1 main article, supporting images and 12 short poems.
We would like the designer to create page vectors, borders, fonts and other layout design elements.

In the first stage of the competition we request:

Magazine layout - 6 pages( 4 article variations based on article content and 2 poem page designs)

We would like to see high impact, striking vectors and design concepts to compliment the article content. See attached bullet point guide to article to help design page themes.

COMPANY INFO
Writer, poet, researcher and commentator. Our client is interested in sharing art and issues he believes in. Our client would like to design one magazine issue first but has a collection of material to produce a series of magazines in the future. So he is looking to establish a potentially long-term partnership with designer(s).

Target Market(s)

Quick and easy to read, coffee time magazine. Target Market: Male 40yrs+, Intellectual, Open Minded.

Industry/Entity Type

Finance

Font styles to use
Serif
Decorative

Requirements
Must have
• Main Article and Poetry: Space for 1 -2 images per page.
A subtle design feature that connects each page.
Primary colors: Jade Green and some Grayscale.
Secondary Colors: 3rd and 4th color open to designers preference.
Page Dimensions : 7.5in height, 7in width.
Articles: Same color theme, different layout and vector choice, same font color and size.
Poetry: Some design creative freedom. Focus on creating a unique title font incorporating the theme of the poem, Poetry TITLE font must be made a feature design element (poem identity)
Font: See Verdant Explorer magazine styling
Columns: Single or multiple.
All vectors and images should be sourced from craft bazaar.
Nice to have
• Images/pictures that connect with article topic and align with color theme.
Should not have
• Avoid repetition of page design. To do this follow the idea of each paragraph (see attached breakdown)

```html
<!DOCTYPE html>
<html lang="en">
<head>
<meta charset="utf-8">
<title>Tovik Lumen – Health Spread</title>
<link rel="stylesheet" href="https://fonts.googleapis.com/css2?family=Arvo:ital,wght@0,700;1,700&family=Tinos:ital,wght@0,400;0,700;1,400;1,700&family=Istok+Web:ital,wght@0,400;1,400;1,700&display=swap">
<style>
  :root{
    --jade:#1e9a69;
    --jade-dark:#157a52;
    --jade-light:#7cc9a5;
    --paper:#fbfbfa;
    --ink:#2b2b2b;
    --grey-bg:#d7d7d7;
    --cream:#f1e7c2;
    --cross-red:#d9232a;
    --caption-red:#c9252b;
  }
  *{box-sizing:border-box;margin:0;padding:0}
  html,body{width:1200px;height:570px;overflow:hidden;background:var(--grey-bg)}
  .spread{position:absolute;left:40px;top:25px;width:1120px;height:520px;background:var(--paper);box-shadow:0 2px 8px rgba(0,0,0,.18)}
  .page{position:absolute;top:0;width:560px;height:520px;overflow:hidden}
  .page--left{left:0}
  .page--right{left:560px;border-left:1px solid #e2e2e2}

  .section-bar{position:absolute;left:0;right:0;top:22px;height:14px;background:var(--jade);border-bottom:3px solid #fff;box-shadow:0 2px 0 var(--jade-light)}
  .section-bar__label{position:absolute;top:1px;font:italic 700 10px/12px "Tinos",serif;color:#fff;letter-spacing:.5px}
  .page--left .section-bar__label{left:28px}
  .page--right .section-bar__label{right:28px}

  .footer{position:absolute;left:0;right:0;bottom:16px;height:30px;background:var(--jade);border-top:4px solid var(--jade-light)}
  .folio{position:absolute;top:7px;font:italic 700 11px/14px "Tinos",serif;color:#fff}
  .page--left .folio{left:20px}
  .page--right .folio{right:20px}
  .folio__bar{display:inline-block;width:1px;height:14px;background:#fff;vertical-align:-3px;margin:0 8px}

  .body-text{font:10.6px/13.4px "Tinos",serif;color:var(--ink);text-align:justify}
  .body-text p{margin-bottom:9px}
  .body-text p:last-child{margin-bottom:0}

  /* left page */
  .title-panel{position:absolute;left:22px;top:58px;width:232px;height:402px;background:var(--jade)}
  .title-panel__heading{position:absolute;left:14px;top:10px;font:700 43px/47px "Arvo",serif;color:#fff;letter-spacing:.5px}
  .title-panel__image{position:absolute;left:12px;top:176px;width:208px;height:148px;background:linear-gradient(180deg,#ffffff,#eef3f8)}
  .title-panel__image-shape{position:absolute;left:84px;top:10px;width:40px;height:128px;border-radius:20px;background:linear-gradient(180deg,#6fa1d6,#2d5fa5)}
  .title-panel__caption{position:absolute;left:10px;right:10px;top:330px;font:italic 10.6px/13.2px "Istok Web",sans-serif;color:#fff;text-align:center}

  .article-lead{position:absolute;left:268px;top:60px;width:268px;height:403px}
  .drop-cap{float:left;font:700 56px/44px "Tinos",serif;color:var(--jade);margin:2px 6px 0 0}

  /* right page */
  .feature-box{position:absolute;left:22px;top:48px;width:322px;height:148px;background:var(--cream)}
  .feature-box__image{position:absolute;left:16px;top:14px;width:118px;height:118px;background:var(--cross-red)}
  .feature-box__text{position:absolute;left:148px;top:14px;width:166px;font:italic 10.6px/13.2px "Istok Web",sans-serif;color:var(--caption-red)}

  .col{position:absolute}
  .col--one{left:22px;top:208px;width:158px}
  .col--two{left:188px;top:208px;width:160px}
  .col--three{left:364px;top:48px;width:178px}

  .pull-quote{position:absolute;left:22px;top:382px;width:326px;height:80px}
  .pull-quote__mark{position:absolute;left:0;top:-8px;font:700 64px/64px "Arvo",serif;color:var(--jade)}
  .pull-quote__text{position:absolute;left:42px;top:2px;right:0;font:italic 10.6px/13.4px "Istok Web",sans-serif;color:var(--jade)}
  .continue-arrow{color:var(--jade);font-weight:700}
</style>
</head>
<body>
<main class="spread">

  <section class="page page--left">
    <div class="section-bar"><span class="section-bar__label">HEALTH</span></div>

    <div class="title-panel">
      <h1 class="title-panel__heading">Doctors<br>Destroy<br>Health</h1>
      <div class="title-panel__image" role="img" aria-label="Illustration of a winged staff with two entwined serpents">
        <div class="title-panel__image-shape"></div>
      </div>
      <p class="title-panel__caption">The international emblem for health depicts two serpents entwined, symbolizing their control over our health system. Symbolism such as this is there for all to see, yet most of us simply don’t see it</p>
    </div>

    <div class="article-lead body-text">
      <p><span class="drop-cap">T</span>he medical establishment around the world is just a tool of the pharmaceutical cartel, or ‘Big Pharma’. The last thing it represents is human health. It couldn’t give a care in the world for it. Mainstream medicine is about wealth, not health, and even more than that, it aims to keep from them a connection to their true and infinite self. Big Pharma works as one network, despite the appearance of apparently different ‘companies’, and its classic Illuminati pyramid-within-pyramid structure controls the entire mainstream medical profession and its associated ‘industry’. In truth, it is an ‘industry’ founded on human suffering, and the more suffering the better. After all, healthy people don’t pay medical bills; sick people do. Big Pharma controls what is taught in the medical schools, the drugs that doctors prescribe, how far they can stray from strictly-enforced medical ‘norms’, and dictates government ‘health’ policy.</p>
      <p>It does this through a range of techniques that include political contributions and bribes to doctors such as all-expenses-paid trips to ‘conferences’ in exotic places that are nothing more than free holidays. Mainstream Big Pharma medicine is a grotesque cesspit of corruption and self-interest made even worse by the extraordinary levels of ignorance and incompetence among those who are paid outrageous sums to be ‘medical experts’.</p>
      <p>Control of the medical schools and governing bodies, and the brutal policing of any practitioners who chal-</p>
    </div>

    <footer class="footer"><span class="folio">4<span class="folio__bar"></span>Tovik Lumen</span></footer>
  </section>

  <section class="page page--right">
    <div class="section-bar"><span class="section-bar__label">HEALTH</span></div>

    <div class="feature-box">
      <div class="feature-box__image" role="img" aria-label="Illustration of a large red cross on a cream label"></div>
      <p class="feature-box__text">The Crimson Aid Society is found throughout the world today. The red cross derives from the Phoenician red cross shield which was brought to Britain where one branch of their people would become the Anglo-Saxons. Today it is still seen on England’s national flag</p>
    </div>

    <div class="col col--one body-text">
      <p>lenge the ‘norms’, means that mainstream doctors don’t even know what works, let alone how to treat it. They simply know what they are taught to know in medical school and they are jumped on immediately if they try to expand their knowledge and act upon it in the way they treat their patients.</p>
    </div>

    <div class="col col--two body-text">
      <p>On a daily basis, doctors kill and maim on a monumental scale worldwide. How insane that doctors are the third biggest cause of death in America after heart disease and cancer with upwards of a quarter of a million people dying in US hospitals every year from unnecessary surgery, misdiagnosis or other mistreatment.</p>
    </div>

    <blockquote class="pull-quote">
      <span class="pull-quote__mark">“</span>
      <p class="pull-quote__text">Drugs have also been used for thousands of years to alter the state of consciousness, and the Central Bureau-British Intelligence networks fund drug research to find more and more effective ways of suppressing consciousness and will. This includes vaccinations, food additives, and electromagnetic exposure.</p>
    </blockquote>

    <div class="col col--three body-text">
      <p>A study in 2009 revealed that more people die because of prescription ‘painkillers’ than the combined total of those who die from the effects of heroin and cocaine.</p>
      <p>The National Remedy Board (NRB) estimates that the Halvorn painkiller, Dolarex, widely used by sufferers of arthritis, may have contributed to 27,785 heart attacks and sudden cardiac deaths between 1999 and 2003 alone.</p>
      <p>Drugs have also been used for thousands of years to alter the state of consciousness, and the Central Bureau-British Intelligence networks fund drug research to find more and more effective ways of suppressing consciousness and will. This includes vaccinations, food additives, and electromagnetic exposure.</p>
      <p>What came about after the H5N1 ‘crisis’ in 2009 brought a seemingly world-wide campaign to get every man, woman and child ‘immunized’ for the ‘swine flu’. Fortunately, people have already woken up to the <span class="continue-arrow">→</span></p>
    </div>

    <footer class="footer"><span class="folio">Tovik Lumen<span class="folio__bar"></span>5</span></footer>
  </section>

</main>
</body>
</html>
```